Business Card design for new private practice opening

I need a business card design for my new private practice with my new logo uploaded as a file
On the front the logo
On the back: maybe a small logo somewhere?
Priv. Doz. DDr. Petra Sommerfeld
Fachärztin für Allgemein- & Viszeralchirurgie
Address: xxx
Tel: xxx
Mobil:xxx
Webseite:xxx
Email:xxx

Contact Information for Business Card

See project description above for details

Requirements
Nice to have
• I would like the colors of the logo incorporated into the business card

```html
<!DOCTYPE html>
<html lang="de">
<head>
<meta charset="utf-8">
<title>Sommerfeld Chirurgie – Visitenkarte</title>
<link href="https://fonts.googleapis.com/css2?family=Montserrat:wght@400;500;700&display=swap" rel="stylesheet">
<style>
  :root{
    --teal:#47bab7;
    --grey:#7b7b7b;
    --ink:#2b2b2b;
    --paper:#ffffff;
    --backdrop:#3a3a3c;
  }
  *{margin:0;padding:0;box-sizing:border-box}
  html,body{width:1200px;height:875px;overflow:hidden}
  body{background:var(--backdrop);font-family:"Montserrat",sans-serif;position:relative}
  .card{position:absolute;width:620px;height:355px;border-radius:22px;overflow:hidden;box-shadow:0 14px 30px rgba(0,0,0,.45)}
  .card--front{left:60px;top:60px;background:var(--teal)}
  .card--back{left:520px;top:460px;background:var(--paper)}

  .front-brand{position:absolute;left:70px;top:110px;display:flex;align-items:center;gap:30px}
  .front-brand__dot{width:135px;height:135px;border-radius:50%;background:var(--paper)}
  .front-brand__name{color:var(--paper);font-weight:700;font-size:44px;line-height:1.05;letter-spacing:1px;text-transform:uppercase}

  .back-brand{position:absolute;left:34px;top:40px;display:flex;align-items:center;gap:12px}
  .back-brand__dot{width:52px;height:52px;border-radius:50%;background:var(--teal)}
  .back-brand__name{color:var(--grey);font-weight:700;font-size:20px;line-height:1.05;text-transform:uppercase;letter-spacing:.5px}

  .doctor{position:absolute;right:32px;top:34px;text-align:right}
  .doctor__name{color:var(--grey);font-weight:700;font-size:19px}
  .doctor__title{color:var(--ink);font-weight:500;font-size:12px;margin-top:3px}

  .emblem{position:absolute;right:58px;top:108px;width:190px;height:190px;border-radius:50%;background:var(--teal)}

  .contact{position:absolute;left:34px;bottom:30px;color:var(--ink);font-size:13px;line-height:1.45}
  .contact__address{margin-bottom:10px}
  .contact__list{list-style:none}
  .contact__item{display:flex;align-items:center;gap:9px}
  .contact__icon{width:13px;height:13px;fill:var(--teal);flex:none}
</style>
</head>
<body>
  <section class="card card--front">
    <div class="front-brand">
      <span class="front-brand__dot"></span>
      <p class="front-brand__name">Sommerfeld<br>Chirurgie</p>
    </div>
  </section>

  <section class="card card--back">
    <div class="back-brand">
      <span class="back-brand__dot"></span>
      <p class="back-brand__name">Sommerfeld<br>Chirurgie</p>
    </div>

    <div class="doctor">
      <p class="doctor__name">Priv. Doz. DDr. Petra Sommerfeld</p>
      <p class="doctor__title">Fachärztin für Allgemein- &amp; Viszeralchirurgie</p>
    </div>

    <div class="emblem"></div>

    <div class="contact">
      <p class="contact__address">48 Linden Court Suite<br>3204 Marlow, PA 19072</p>
      <ul class="contact__list">
        <li class="contact__item">
          <svg class="contact__icon" viewBox="0 0 24 24"><path d="M6.6 10.8a15.1 15.1 0 0 0 6.6 6.6l2.2-2.2a1 1 0 0 1 1-.25 11.4 11.4 0 0 0 3.6.57 1 1 0 0 1 1 1V20a1 1 0 0 1-1 1A17 17 0 0 1 3 4a1 1 0 0 1 1-1h3.5a1 1 0 0 1 1 1c0 1.25.2 2.45.57 3.57a1 1 0 0 1-.25 1z"/></svg>
          (610) 555-0142
        </li>
        <li class="contact__item">
          <svg class="contact__icon" viewBox="0 0 24 24"><rect x="6" y="2" width="12" height="20" rx="2"/><rect x="8" y="5" width="8" height="11" fill="#fff"/></svg>
          (610) 555-0187
        </li>
        <li class="contact__item">
          <svg class="contact__icon" viewBox="0 0 24 24"><path d="M2 5h20v14H2z"/><path d="M2 5l10 8 10-8" fill="none" stroke="#fff" stroke-width="2"/></svg>
          praxis@sommerfeld-mail.com
        </li>
        <li class="contact__item">
          <svg class="contact__icon" viewBox="0 0 24 24"><circle cx="12" cy="12" r="10"/><path d="M2 12h20M12 2c3 3 3 17 0 20M12 2c-3 3-3 17 0 20" fill="none" stroke="#fff" stroke-width="1.5"/></svg>
          www.sommerfeld-praxis.com
        </li>
      </ul>
    </div>
  </section>
</body>
</html>
```